Allied Health Clinic needs catchy poster ad for lightbox

We need a catchy and effective poster designed for our retail lightbox which is in a busy corridor. We are a multi disciplinary sports injury clinic offering a range of allied health services. Established in 1999. We need people to understand our business identity and services clearly. I have come up with a very rough idea as far as what I think the copy should contain. The picture is an example of what image I am trying to convey to the potential client. I am not a designer clearly. We specialise in treating difficult problems.
Size of the poster is 451mm x 741mm at 300dpi. We will then blow the image up to double this size which will be good enough resolution for the printing.

Target Market(s)

White collar professionals - male and female, active 20-50 range

Industry/Entity Type

Healthcare

Font styles to use
Sans Serif

Requirements
Nice to have
• Easy to read, polished, nice tie in to my logo colours

```html
<!DOCTYPE html>
<html lang="en">
<head>
<meta charset="utf-8">
<title>Corestride Physiotherapy – Injury Experts</title>
<link href="https://fonts.googleapis.com/css2?family=Roboto+Condensed:wght@700&display=swap" rel="stylesheet">
<style>
  :root {
    --green: #8cc63f;
    --charcoal: #4a4a4c;
    --swoosh-light: #e4e4e6;
    --ink: #1e1e1e;
    --slate: #3d3d3f;
    --paper: #ffffff;
  }
  * { margin: 0; padding: 0; box-sizing: border-box; }
  html, body { width: 933px; height: 1200px; overflow: hidden; background: var(--paper); }
  .poster {
    position: relative;
    width: 933px;
    height: 1200px;
    overflow: hidden;
    background: var(--paper);
    font-family: "Roboto Condensed", "Arial Narrow", sans-serif;
    font-weight: 700;
    text-transform: uppercase;
  }
  .shapes { position: absolute; inset: 0; }
  .headline {
    position: absolute; left: 0; right: 0; top: 20px;
    text-align: center; color: var(--green);
    font-size: 96px; line-height: 1; letter-spacing: 7px;
  }
  .tagline {
    position: absolute; left: 0; right: 0; top: 112px;
    text-align: center; color: var(--slate);
    font-size: 45px; line-height: 1; letter-spacing: 3px;
  }
  .hero-art {
    position: absolute; left: 16px; top: 172px; width: 560px; height: 465px;
    border-radius: 40% 50% 45% 40%;
    background: radial-gradient(ellipse at 55% 45%, #f25a8c 0%, #b04fc0 35%, #7ec8f0 62%, rgba(255,255,255,0) 76%);
    opacity: 0.85;
  }
  .claim {
    position: absolute; left: 583px; top: 364px;
    color: var(--ink);
  }
  .claim .lead { font-size: 38px; line-height: 1.1; letter-spacing: 3px; }
  .claim .big { font-size: 47px; line-height: 1.02; letter-spacing: 2px; margin-top: 2px; }
  .claim .since { font-size: 26px; line-height: 1; letter-spacing: 1px; margin-top: 4px; }
  .range {
    position: absolute; left: 223px; top: 654px;
    color: var(--ink); font-size: 39px; line-height: 1.04; letter-spacing: 2px;
  }
  .range .line1 { padding-left: 30px; }
  .services { list-style: none; }
  .services li {
    position: absolute; height: 38px; color: var(--paper);
    font-size: 38px; line-height: 38px; letter-spacing: 1px;
    display: flex; align-items: center; gap: 18px; white-space: nowrap;
  }
  .services li::before {
    content: ""; width: 30px; height: 30px; border-radius: 50%;
    background: var(--green); flex: none;
  }
  .brand-dot {
    position: absolute; left: 72px; top: 925px;
    width: 56px; height: 56px; border-radius: 50%; background: var(--green);
  }
  .brand {
    position: absolute; left: 61px; top: 1040px;
    color: var(--slate); font-size: 26px; line-height: 1.1; letter-spacing: 4.5px;
  }
  .contact {
    position: absolute; right: 28px; top: 1106px;
    text-align: right; color: var(--paper); line-height: 1;
  }
  .contact .directions { font-size: 37px; }
  .contact .details { font-size: 40px; letter-spacing: 2px; margin-top: 4px; }
  .contact .web { text-transform: none; }
</style>
</head>
<body>
<main class="poster">
  <svg class="shapes" width="933" height="1200" viewBox="0 0 933 1200" aria-hidden="true">
    <path d="M35 709 C 260 785 620 760 933 510 L 933 527 C 620 778 260 806 35 709 Z" fill="var(--swoosh-light)"/>
    <path d="M35 709 C 260 806 620 778 933 527 L 933 1030 C 780 1030 600 1030 470 1018 C 230 966 90 820 35 709 Z" fill="var(--charcoal)"/>
    <path d="M0 1200 C 300 1120 600 1095 933 1088 L 933 1200 Z" fill="var(--green)"/>
  </svg>

  <h1 class="headline">Injury Experts</h1>
  <p class="tagline">Trusted by Athletes</p>

  <div class="hero-art" role="img" aria-label="Colourful paint-splash illustration of a footballer kicking a ball"></div>

  <div class="claim">
    <div class="lead">Successfully</div>
    <div class="big">Treating<br>Difficult<br>Injuries</div>
    <div class="since">Since 1999</div>
  </div>

  <div class="range">
    <div class="line1">A Complete</div>
    <div>Range of Services</div>
  </div>

  <ul class="services">
    <li style="left:137px; top:789px;">Sports Physiotherapy</li>
    <li style="left:194px; top:834px;">Chiropractic</li>
    <li style="left:258px; top:880px;">Massage</li>
    <li style="left:344px; top:923px;">Podiatry</li>
    <li style="left:465px; top:967px;">Exercise Physiology</li>
  </ul>

  <span class="brand-dot" aria-hidden="true"></span>
  <div class="brand">Corestride Physiotherapy<br>&amp; Sports Injury Clinic</div>

  <div class="contact">
    <div class="directions">Take lifts to level 8</div>
    <div class="details">8640 2175 | <span class="web">corestridephysio.com.au</span></div>
  </div>
</main>
</body>
</html>
```